Stationery Design Project

We are a start up wine business based in Sydney Australia. We already have a logo and are in the process of completing our website. We require our logo to be cleverly and artfully incorporated into our stationary requirements. Which will initially begin with a company letter head.
As we desire consistency across our brand, we will also be wanting to develop banner advertisements and brochure with the same "look".
If outstanding we move design brief to banner advertisement for web and banner of the website itself.
Target Market(s)
Older wealthy predominantly male demographic
Industry/Entity Type
Business
Look and feel

```html
<!DOCTYPE html>
<html lang="en">
<head>
<meta charset="utf-8">
<title>Marlowe Bay Estate — Letterhead</title>
<link rel="stylesheet" href="https://fonts.googleapis.com/css2?family=Questrial&display=swap">
<style>
  :root {
    --paper: #ffffff;
    --ink: #1b1b1b;
    --label: #5a5a5a;
    --detail: #9a9a9a;
    --rule: #d4d4d4;
  }
  html, body {
    margin: 0;
    padding: 0;
    width: 1019px;
    height: 1200px;
    overflow: hidden;
    background: var(--paper);
  }
  .letterhead {
    position: relative;
    width: 1019px;
    height: 1200px;
    background: var(--paper);
    font-family: "Questrial", Arial, sans-serif;
  }
  .brand {
    position: absolute;
    top: 112px;
    left: 0;
    right: 0;
    margin: 0;
    text-align: center;
    color: var(--ink);
    font-size: 30px;
    line-height: 40px;
    font-weight: 400;
    letter-spacing: 1px;
    white-space: nowrap;
  }
  .footer {
    position: absolute;
    left: 72px;
    right: 76px;
    top: 1138px;
    height: 56px;
  }
  .address {
    margin: 0;
    text-align: center;
    font-size: 13px;
    line-height: 16px;
    color: var(--detail);
  }
  .rule {
    height: 1px;
    background: var(--rule);
    margin: 6px 0 9px;
  }
  .contact {
    display: flex;
    justify-content: center;
    gap: 34px;
    margin: 0;
    padding: 0;
    list-style: none;
    font-size: 13px;
    line-height: 16px;
    white-space: nowrap;
  }
  .contact .label { color: var(--label); }
  .contact .value { color: var(--detail); }
</style>
</head>
<body>
  <main class="letterhead">
    <h1 class="brand">Marlowe Bay Estate</h1>

    <footer class="footer">
      <p class="address">Street Name, City, State, zip code</p>
      <div class="rule"></div>
      <ul class="contact">
        <li><span class="label">Phone:</span> <span class="value">123-456-7890</span></li>
        <li><span class="label">Fax:</span> <span class="value">123-456-7890</span></li>
        <li><span class="label">Email:</span> <span class="value">hello@marlowebay.com</span></li>
        <li><span class="label">Web:</span> <span class="value">www.marlowebay.com</span></li>
      </ul>
    </footer>
  </main>
</body>
</html>
```